Lantern Holdings Business Card

We are looking to design new business cards for our company. We have two office locations and would like to have both full addresses on the card. Each address needs two lines for the building name and street address and a line or two for the city, state and zip code. There should be a place for 2-3 phone numbers. The addresses and phone numbers are at the bottom of this description. We also need a place to put our company website and one email address. Our logo is attached.
We would like the card to be two sided. The back of the card should have a blue background with some part of our logo design on it. We would like the full logo on the front of the card as well. The front of the card should have a white background with the blue logo. We are open to listing our addresses on the front or the back of the card. The person who designed our logo gave us an excellent business card idea that we really liked. I have attached a picture of his business card idea so that we can build off of it.
Addresses:
The Marlow Exchange
2214 47th Street NW
Washington, DC 20419
Osprey Harbor Tower
815 Tamsin Boulevard #2207
Miami, FL 33987
Phone Numbers: (202) 555-0148
(202) 555-0193
Website: www.lanternholdings-example.com

```html
<!DOCTYPE html>
<html lang="en">
<head>
<meta charset="utf-8">
<title>Lantern Holdings Business Card</title>
<link href="https://fonts.googleapis.com/css2?family=Arimo:wght@400;700&display=swap" rel="stylesheet">
<style>
  :root {
    --stage: #eef0f2;
    --brand-blue: #1a0fe0;
    --brand-blue-soft: #2a22ee;
    --brand-deep: #0b0760;
    --stripe-dark: #14141e;
    --paper: #ffffff;
    --ink-light: #ffffff;
    --mark-dark: #1c1c28;
  }
  * { margin: 0; padding: 0; box-sizing: border-box; }
  html, body {
    width: 1200px; height: 923px; overflow: hidden;
    background: var(--stage);
    font-family: "Arimo", Arial, sans-serif;
  }
  .sheet { position: relative; width: 1200px; height: 923px; }
  .card {
    position: absolute; width: 520px; height: 297px; overflow: hidden;
    box-shadow: 0 6px 14px rgba(0,0,0,0.25);
  }
  .card--front-a { left: 40px;  top: 115px; }
  .card--back-a  { left: 640px; top: 115px; }
  .card--front-b { left: 40px;  top: 512px; }
  .card--back-b  { left: 640px; top: 512px; }

  /* Front */
  .card--front { background: var(--paper); }
  .front-band { position: absolute; left: 0; top: 0; width: 200px; height: 297px; }
  .brand { position: absolute; left: 226px; top: 108px; display: flex; align-items: center; gap: 10px; }
  .brand-square { width: 40px; height: 40px; border-radius: 4px; background: var(--brand-blue); }
  .card--front-b .brand-square { background: var(--mark-dark); }
  .brand-name {
    color: var(--brand-blue); font-weight: 400; font-size: 29px; letter-spacing: 0.5px; white-space: nowrap;
  }
  .website {
    position: absolute; left: 226px; top: 160px;
    color: var(--brand-blue); font-weight: 700; font-size: 13.5px; letter-spacing: 0.1px;
  }

  /* Back */
  .card--back { background: var(--brand-blue); }
  .back-panel {
    position: absolute; left: 262px; top: 26px; width: 290px; height: 232px;
    border-radius: 26px; background: var(--brand-blue-soft);
  }
  .contact {
    position: absolute; left: 70px; top: 128px; color: var(--ink-light);
    font-size: 11.5px; line-height: 1.28;
  }
  .contact-block { margin-bottom: 10px; }
  .contact-label { font-weight: 700; }
</style>
</head>
<body>
<main class="sheet">

  <section class="card card--front card--front-a">
    <svg class="front-band" viewBox="0 0 200 297" aria-hidden="true">
      <defs>
        <linearGradient id="bandShadeA" x1="0" y1="1" x2="1" y2="0">
          <stop offset="0" stop-color="#0b0760"/>
          <stop offset="0.6" stop-color="#1a0fe0"/>
        </linearGradient>
      </defs>
      <rect width="200" height="297" fill="url(#bandShadeA)"/>
      <path d="M0 22 C70 26 150 40 200 60" stroke="#14141e" stroke-width="5" fill="none"/>
      <path d="M0 40 C80 46 150 66 200 92" stroke="#1a0fe0" stroke-width="9" fill="none"/>
      <path d="M0 58 C80 66 150 92 200 130" stroke="#14141e" stroke-width="10" fill="none"/>
      <path d="M0 80 C80 92 150 124 200 176" stroke="#1a0fe0" stroke-width="7" fill="none"/>
    </svg>
    <div class="brand"><span class="brand-square"></span><span class="brand-name">Lantern Holdings</span></div>
    <p class="website">www.lanternholdings-example.com</p>
  </section>

  <section class="card card--back card--back-a">
    <div class="back-panel"></div>
    <div class="contact">
      <div class="contact-block"><div class="contact-label">The Marlow Exchange</div><div>2214 47th Street NW</div><div>Washington, DC 20419</div></div>
      <div class="contact-block"><div class="contact-label">Osprey Harbor Tower</div><div>815 Tamsin Boulevard #2207</div><div>Miami, FL 33987</div></div>
      <div class="contact-block"><div class="contact-label">Phone Numbers:</div><div>(202) 555-0148 / (202) 555-0193</div></div>
    </div>
  </section>

  <section class="card card--front card--front-b">
    <svg class="front-band" viewBox="0 0 200 297" aria-hidden="true">
      <defs>
        <linearGradient id="bandShadeB" x1="0" y1="1" x2="1" y2="0">
          <stop offset="0" stop-color="#0b0760"/>
          <stop offset="0.6" stop-color="#1a0fe0"/>
        </linearGradient>
      </defs>
      <rect width="200" height="297" fill="url(#bandShadeB)"/>
      <path d="M0 22 C70 26 150 40 200 60" stroke="#14141e" stroke-width="5" fill="none"/>
      <path d="M0 40 C80 46 150 66 200 92" stroke="#1a0fe0" stroke-width="9" fill="none"/>
      <path d="M0 58 C80 66 150 92 200 130" stroke="#14141e" stroke-width="10" fill="none"/>
      <path d="M0 80 C80 92 150 124 200 176" stroke="#1a0fe0" stroke-width="7" fill="none"/>
    </svg>
    <div class="brand"><span class="brand-square"></span><span class="brand-name">Lantern Holdings</span></div>
    <p class="website">www.lanternholdings-example.com</p>
  </section>

  <section class="card card--back card--back-b">
    <div class="back-panel"></div>
    <div class="contact">
      <div class="contact-block"><div class="contact-label">The Marlow Exchange</div><div>2214 47th Street NW</div><div>Washington, DC 20419</div></div>
      <div class="contact-block"><div class="contact-label">Osprey Harbor Tower</div><div>815 Tamsin Boulevard #2207</div><div>Miami, FL 33987</div></div>
      <div class="contact-block"><div class="contact-label">Phone Numbers:</div><div>(202) 555-0148 / (202) 555-0193</div></div>
    </div>
  </section>

</main>
</body>
</html>
```